Need to drive pregnant women to my 3d4d ultrasound studio where i provide 4d ultrasound with hyperalistic imaging and gender reveals

Industry/Entity Type

Healthcare

Font styles to use
Decorative
Script

Requirements
Must have
• My Company name Luz de Nueve Lunas 4D. EVERYTHING HAS TO BE IN SPANISH
Nice to have
• SIMPLE AND NOT TOO BUSY
Should not have
• website

```html
<!DOCTYPE html>
<html lang="es">
<head>
<meta charset="utf-8">
<title>Luz de Nueve Lunas 4D</title>
<link href="https://fonts.googleapis.com/css2?family=Cinzel+Decorative:wght@700&family=Dancing+Script:wght@700&display=swap" rel="stylesheet">
<style>
  :root {
    --stage: #a0a0a0;
    --paper: #ffffff;
    --ink: #000000;
    --ink-light: #ffffff;
    --band-dark: #000000;
    --band-sheen: #5a5b5d;
    --silver-light: #f2f2f2;
    --silver-mid: #b9b9b9;
    --silver-dark: #6f6f6f;
    --scan-amber: #c8711f;
    --scan-deep: #5a2a06;
    --skin-light: #f1c6b5;
    --skin-deep: #b97a6c;
  }
  html, body {
    margin: 0;
    padding: 0;
    width: 1200px;
    height: 600px;
    overflow: hidden;
    background: var(--stage);
  }
  .banner {
    position: absolute;
    left: 79px;
    top: 154px;
    width: 1043px;
    height: 304px;
    background: var(--paper);
    box-shadow: 1px 2px 3px rgba(0,0,0,0.35);
    overflow: hidden;
  }
  .banner__art {
    position: absolute;
    inset: 0;
    width: 100%;
    height: 100%;
  }
  .banner__title {
    position: absolute;
    left: 58px;
    top: 30px;
    margin: 0;
    font-family: "Cinzel Decorative", "Times New Roman", serif;
    font-weight: 700;
    font-size: 46px;
    line-height: 58px;
    letter-spacing: 0.5px;
    color: var(--ink-light);
    text-transform: uppercase;
    white-space: nowrap;
  }
  .banner__tagline {
    position: absolute;
    left: 58px;
    top: 194px;
    margin: 0;
    font-family: "Dancing Script", "Brush Script MT", cursive;
    font-weight: 700;
    font-size: 34px;
    line-height: 40px;
    color: var(--ink);
    white-space: nowrap;
  }
</style>
</head>
<body>
  <section class="banner">
    <svg class="banner__art" viewBox="0 0 1738 506" preserveAspectRatio="none">
      <defs>
        <linearGradient id="band-sheen" x1="0" y1="0" x2="1" y2="0">
          <stop offset="0" stop-color="var(--band-dark)"/>
          <stop offset="0.2" stop-color="var(--band-dark)"/>
          <stop offset="0.38" stop-color="var(--band-sheen)"/>
          <stop offset="0.6" stop-color="var(--band-dark)"/>
          <stop offset="1" stop-color="var(--band-dark)"/>
        </linearGradient>
        <linearGradient id="silver-down" x1="0" y1="0" x2="0" y2="1">
          <stop offset="0" stop-color="var(--silver-dark)"/>
          <stop offset="0.45" stop-color="var(--silver-light)"/>
          <stop offset="1" stop-color="var(--silver-mid)"/>
        </linearGradient>
        <linearGradient id="silver-up" x1="0" y1="1" x2="0" y2="0">
          <stop offset="0" stop-color="var(--silver-dark)"/>
          <stop offset="0.45" stop-color="var(--silver-light)"/>
          <stop offset="1" stop-color="var(--silver-mid)"/>
        </linearGradient>
        <radialGradient id="scan-tone" cx="0.4" cy="0.5" r="0.7">
          <stop offset="0" stop-color="var(--scan-amber)"/>
          <stop offset="1" stop-color="var(--scan-deep)"/>
        </radialGradient>
        <radialGradient id="skin-tone" cx="0.5" cy="0.5" r="0.7">
          <stop offset="0" stop-color="var(--skin-light)"/>
          <stop offset="1" stop-color="var(--skin-deep)"/>
        </radialGradient>
      </defs>

      <path class="band-dark" fill="url(#band-sheen)"
            d="M0 0 H887 L995 225 Q1010 260 995 295 L887 506 H0 Z"/>

      <path class="panel-light" fill="var(--paper)"
            d="M0 292 H920 Q955 295 940 330 L847 506 H0 Z"/>

      <polygon class="chevron-top" fill="url(#silver-down)" points="902,0 1034,0 967,109"/>
      <polygon class="chevron-bottom" fill="url(#silver-up)" points="902,506 1034,506 967,399"/>

      <rect class="photo photo--scan" x="1067" y="60" width="298" height="395"
            fill="url(#scan-tone)" role="img" aria-label="Ecografía 4D del bebé en el vientre"/>
      <rect class="photo photo--newborn" x="1374" y="60" width="298" height="395"
            fill="url(#skin-tone)" role="img" aria-label="Fotografía de un recién nacido dormido"/>
    </svg>

    <h1 class="banner__title">Luz de Nueve<br>Lunas 4D</h1>
    <p class="banner__tagline">Ecografías 4D hiperrealistas<br>y revelación de género</p>
  </section>
</body>
</html>
```